business card for a shoe shop

we would like a business card for a family owned shoe shop.
With this information included.
Darnell's Shoe Store
Family owned since 1947

then on other side
Darnell's Shoe Store
Footwear fitting specialist
Phone: 9187 2630
218 Quarry St, Fernleigh Downs 3187
(cnr. Hartwick Rd and Quarry St)
darnellshoes218@examplemail.com
if could incorporate the purple color on card i have attached.

```html
<!DOCTYPE html>
<html lang="en">
<head>
<meta charset="utf-8">
<title>Darnell's Shoe Store – Business Card</title>
<link href="https://fonts.googleapis.com/css2?family=Arimo:wght@400&family=Montserrat:wght@400;600&family=Marcellus&display=swap" rel="stylesheet">
<style>
  :root {
    --backdrop: #f7f3b4;
    --brand-purple: #735aa6;
    --card-white: #ffffff;
    --text-grey: #5f5f5f;
  }
  * { box-sizing: border-box; margin: 0; padding: 0; }
  html, body {
    width: 1200px;
    height: 1200px;
    overflow: hidden;
    background: var(--backdrop);
    font-family: "Arimo", Arial, sans-serif;
  }
  .canvas {
    position: relative;
    width: 1200px;
    height: 1200px;
  }
  .card {
    position: absolute;
    top: 480px;
    width: 420px;
    height: 240px;
    border-radius: 18px;
    overflow: hidden;
  }
  .card--front {
    left: 156px;
    background: var(--card-white);
  }
  .card--back {
    left: 624px;
    background: var(--brand-purple);
  }

  /* Wordmark */
  .wordmark {
    position: absolute;
    font-family: "Montserrat", Arial, sans-serif;
    line-height: 1;
  }
  .wordmark__name {
    display: block;
    font-weight: 600;
  }
  .wordmark__sub {
    display: block;
    font-weight: 400;
    letter-spacing: 0.12em;
  }
  .card--front .wordmark {
    right: 16px;
    top: 18px;
    text-align: right;
    color: var(--brand-purple);
  }
  .card--front .wordmark__name { font-size: 34px; }
  .card--front .wordmark__sub { font-size: 14px; margin-top: 8px; }

  .card--back .wordmark {
    left: 0;
    right: 0;
    top: 82px;
    text-align: center;
    color: var(--card-white);
  }
  .card--back .wordmark__name { font-size: 44px; }
  .card--back .wordmark__sub { font-size: 17px; margin-top: 10px; }

  /* Front details */
  .specialty {
    position: absolute;
    right: 16px;
    top: 156px;
    font-size: 14px;
    color: var(--text-grey);
  }
  .divider {
    position: absolute;
    left: 16px;
    right: 16px;
    top: 182px;
    height: 1px;
    background: var(--brand-purple);
  }
  .contact {
    position: absolute;
    left: 16px;
    top: 194px;
    font-size: 11.5px;
    line-height: 15px;
    color: var(--text-grey);
    list-style: none;
  }
  .contact__item {
    display: flex;
    align-items: center;
    gap: 5px;
  }
  .contact__icon {
    width: 11px;
    height: 11px;
    flex: none;
    fill: var(--brand-purple);
  }
  .address {
    position: absolute;
    right: 16px;
    top: 196px;
    font-size: 11.5px;
    line-height: 15px;
    text-align: right;
    color: var(--text-grey);
    font-style: normal;
  }

  /* Back band */
  .heritage-band {
    position: absolute;
    left: 0;
    right: 0;
    top: 205px;
    height: 20px;
    background: var(--card-white);
    display: flex;
    align-items: center;
    justify-content: center;
    font-family: "Marcellus", Georgia, serif;
    font-size: 10px;
    letter-spacing: 0.28em;
    color: var(--brand-purple);
  }
</style>
</head>
<body>
<main class="canvas">
  <section class="card card--front" aria-label="Business card front">
    <div class="wordmark">
      <span class="wordmark__name">Darnell's</span>
      <span class="wordmark__sub">SHOE STORE</span>
    </div>
    <p class="specialty">Footwear fitting specialist</p>
    <div class="divider"></div>
    <ul class="contact">
      <li class="contact__item">
        <svg class="contact__icon" viewBox="0 0 24 24" aria-hidden="true"><path d="M6.6 10.8a15.1 15.1 0 0 0 6.6 6.6l2.2-2.2a1 1 0 0 1 1-.25 11.4 11.4 0 0 0 3.6.57 1 1 0 0 1 1 1V20a1 1 0 0 1-1 1A17 17 0 0 1 3 4a1 1 0 0 1 1-1h3.5a1 1 0 0 1 1 1c0 1.25.2 2.45.57 3.57a1 1 0 0 1-.25 1z"/></svg>
        <span>9187 2630</span>
      </li>
      <li class="contact__item">
        <svg class="contact__icon" viewBox="0 0 24 24" aria-hidden="true"><path d="M2 5h20v14H2z M2 5l10 8 10-8" fill="none" stroke="#735aa6" stroke-width="2.4"/></svg>
        <span>darnellshoes218@examplemail.com</span>
      </li>
    </ul>
    <address class="address">
      218 Quarry St, Fernleigh Downs 3187<br>
      (cnr. Hartwick Rd and Quarry St)
    </address>
  </section>

  <section class="card card--back" aria-label="Business card back">
    <div class="wordmark">
      <span class="wordmark__name">Darnell's</span>
      <span class="wordmark__sub">SHOE STORE</span>
    </div>
    <div class="heritage-band">FAMILY OWNED SINCE 1947</div>
  </section>
</main>
</body>
</html>
```